develop our online residential property development appraisal service

This project requires a detailed WordPress design to represent a new digital residential property development consultancy business. At its heart it will have a number of different products that essentially advise customers of the potential value and feasibility of developing their residential site into multiple townhouses, units, apartments, etc... This will be accompanied by explaining the considerations of residential property development.

We aim to navigate and break down this complex area and provide our customers with the tools, knowledge, control and power to 'unlock the value' in their property.

REFERENCE DOCUMENTS:
1. Detailed solution requirements please refer to the attached 'wordpressdesignrequirements'
2. Logo files, style guide and colour pallet please refer to the attached 'QRBT.zip'
3. Site Map refer to attached 'wordpressdesignsitemap'
Updates

Reason: Additional information provided so extending period for designs to take into account.

Target Market(s)

The site will appeal to professional service providers; accountants, financial planners, lawyers, etc…

Industry/Entity Type

Residential

Font styles to use
Sans Serif
Other font styles liked:
• Similar to the logo font, slim line and simple

Requirements
Must have
• The logo, style and colour palette provided in the attached 'QRBT.zip' files
• Satisfy the intent of the 'wordpressdesignrequirements'
• Present as an online-centric business
• Clean, crisp and modern design
• Predominant use of white as a background contrasted with the colours provided in the colour palette
Nice to have
• Use of the following WordPress business themes is encouraged but not mandatory:
• 1. Tovy
• 2. Palex
• 3. Munk
Should not have
• Overt references to Australia

```html
<!DOCTYPE html>
<html lang="en">
<head>
<meta charset="utf-8">
<title>QRBT Property Development Appraisals</title>
<link href="https://fonts.googleapis.com/css2?family=Open+Sans:wght@300;400;600;700;800&display=swap" rel="stylesheet">
<style>
:root{
  --green:#1a9a72;
  --green-dark:#14805e;
  --ink:#333;
  --muted:#555;
  --light:#f3f3f3;
  --footer:#1e1e1e;
  --footer-base:#121212;
  --white:#fff;
}
*{margin:0;padding:0;box-sizing:border-box}
html,body{width:1200px;height:2990px;overflow:hidden}
body{font-family:"Open Sans",Arial,sans-serif;color:var(--ink);background:var(--white);position:relative}
.abs{position:absolute}
a{color:inherit;text-decoration:none}

/* header */
.site-header{position:absolute;left:0;top:0;width:1200px;height:104px;background:var(--white)}
.brand{position:absolute;left:122px;top:30px;display:flex;align-items:center;gap:14px}
.brand-name{font-size:38px;font-weight:300;color:var(--green);letter-spacing:3px}
.brand-tag{font-size:12px;font-weight:400;color:#9aa;line-height:1.3;border-left:1px solid #ccd;padding-left:10px}
.main-nav{position:absolute;top:42px;left:0;font-size:14px;color:#444}
.main-nav a{position:absolute;white-space:nowrap}
.search-btn{position:absolute;left:1046px;top:38px;width:30px;height:30px;border-radius:50%;background:var(--green)}

/* hero */
.hero{position:absolute;left:0;top:104px;width:1200px;height:520px;background:linear-gradient(180deg,#5f8a3e 0%,#7d6a52 35%,#8a4a35 60%,#5c9a2e 80%,#6fb03a 100%)}
.hero-title{position:absolute;left:0;width:1200px;top:292px;text-align:center;color:var(--white);font-size:40px;font-weight:300;text-shadow:0 1px 4px rgba(0,0,0,.4)}
.hero-dots{position:absolute;top:490px;left:564px;display:flex;gap:8px}
.hero-dots span{width:10px;height:10px;border-radius:50%;background:#333}
.hero-dots span.on{background:var(--green)}

/* section headings */
.section-title{position:absolute;left:0;width:1200px;text-align:center;color:var(--green);font-size:26px;font-weight:700}
.intro{position:absolute;left:120px;width:966px;text-align:center;font-size:13.5px;line-height:26px;color:var(--muted)}

/* report cards */
.report-photo{position:absolute;top:804px;width:310px;height:182px}
.report-title{position:absolute;top:1008px;font-size:15px;font-weight:700;color:var(--green)}
.report-text{position:absolute;top:1044px;width:310px;font-size:12px;line-height:21px;color:var(--muted)}
.btn{position:absolute;background:var(--green);color:var(--white);font-size:13px;font-weight:700;text-align:center;border-radius:2px}
.report-btn{top:1130px;width:200px;height:40px;line-height:40px}

/* feature band */
.feature{position:absolute;left:0;top:1248px;width:1200px;height:576px;background:linear-gradient(90deg,#6f5a4a 0%,#b79880 30%,#c8c3b8 55%,#7c8a6a 75%,#5f8a3a 100%)}
.feature-panel{position:absolute;left:698px;top:108px;width:336px;height:368px;background:rgba(20,20,20,.78);padding:34px 18px 0 16px;color:var(--white)}
.feature-panel h2{font-size:29px;font-weight:700;line-height:36px}
.feature-panel p{font-size:13px;line-height:26px;margin-top:16px}
.feature-panel .btn{left:16px;top:314px;width:122px;height:40px;line-height:40px}

/* pages & opportunities */
.col-title{position:absolute;top:1894px;font-size:25px;font-weight:700;color:var(--green)}
.page-thumb{position:absolute;left:104px;width:150px;height:128px}
.page-title{position:absolute;left:272px;font-size:16px;color:var(--green)}
.page-text{position:absolute;left:272px;width:350px;font-size:11.5px;line-height:20px;color:var(--muted)}
.link{position:absolute;font-size:12px;color:var(--green);text-decoration:underline}
.tick{position:absolute;left:674px;width:26px;height:26px}
.opp-title{position:absolute;left:708px;font-size:15px;color:#333}
.opp-text{position:absolute;left:708px;font-size:11.5px;line-height:20px;color:var(--muted);width:340px}

/* about */
.about{position:absolute;left:0;top:2344px;width:1200px;height:388px;background:var(--light)}
.about-icon{position:absolute;width:56px;height:56px;border:2px solid var(--green);border-radius:50%}
.about-head{position:absolute;font-size:16px;color:#444}
.about-head b{color:var(--green);font-weight:700}
.about-text{position:absolute;width:300px;font-size:12px;line-height:22px;color:var(--muted)}

/* footer */
.site-footer{position:absolute;left:0;top:2732px;width:1200px;height:216px;background:var(--footer);color:#ddd}
.foot-title{position:absolute;top:30px;font-size:15px;font-weight:600;color:var(--white)}
.foot-list{position:absolute;list-style:none;font-size:12px;line-height:20px;color:#ddd}
.foot-list li{padding-left:24px;position:relative}
.foot-list.chev li::before{content:">";position:absolute;left:0}
.foot-list.social li::before{content:"";position:absolute;left:2px;top:7px;width:7px;height:7px;border-radius:50%;background:#ddd}
.foot-brand{position:absolute;left:790px;top:26px;font-size:56px;font-weight:300;color:#2f4a40;letter-spacing:4px}
.search-label{position:absolute;left:796px;top:100px;font-size:14px;color:var(--white)}
.search-field{position:absolute;left:796px;top:130px;width:278px;height:34px;background:#111}
.search-go{position:absolute;right:0;top:0;width:38px;height:34px;background:var(--green)}
.foot-small{position:absolute;left:798px;top:180px;font-size:10px;color:#ccc}
.footer-base{position:absolute;left:0;top:2948px;width:1200px;height:42px;background:var(--footer-base);color:#999;font-size:10px;text-align:center;line-height:42px}
</style>
</head>
<body>

<header class="site-header">
  <div class="brand">
    <span class="brand-name">QRBT</span>
    <span class="brand-tag">QRBT Property<br>Development Appraisals</span>
  </div>
  <nav class="main-nav">
    <a style="left:432px">Home</a>
    <a style="left:511px">About Us</a>
    <a style="left:606px">Social Integration</a>
    <a style="left:742px">Property Development Overview</a>
    <a style="left:957px">Contact Us</a>
  </nav>
  <div class="search-btn">
    <svg width="30" height="30" viewBox="0 0 30 30"><circle cx="14" cy="14" r="5" fill="none" stroke="#fff" stroke-width="2"/><line x1="17.5" y1="17.5" x2="21" y2="21" stroke="#fff" stroke-width="2"/></svg>
  </div>
</header>

<section class="hero" role="img" aria-label="Brick family home with a green lawn under large trees">
  <h1 class="hero-title">QRBT Property Development Appraisals</h1>
  <div class="hero-dots"><span class="on"></span><span></span><span></span><span></span></div>
</section>

<h2 class="section-title" style="top:674px">PROPERTY REPORT</h2>
<p class="intro" style="top:722px">Lorem Ipsum is simply dummy text of the printing and typesetting industry. Lorem Ipsum has been the industry's standard dummy text ever since the 1500s, when an unknown printer took a galley of type and scrambled it to make a type specimen book.</p>

<div class="report-photo" style="left:112px;background:linear-gradient(180deg,#4f8fd0,#c9d3dc 60%,#8c8f8a)" role="img" aria-label="Modern white two-storey house"></div>
<div class="report-photo" style="left:448px;background:linear-gradient(180deg,#8ab8e0,#b38a6e 55%,#5d8a3c)" role="img" aria-label="Suburban house with garden"></div>
<div class="report-photo" style="left:782px;background:linear-gradient(180deg,#4a8fd8,#a97a5e 50%,#4f9a34)" role="img" aria-label="Large family home with flower beds"></div>

<h3 class="report-title" style="left:108px">PROPERTY REPORT A</h3>
<h3 class="report-title" style="left:446px">PROPERTY REPORT B</h3>
<h3 class="report-title" style="left:780px">PROPERTY REPORT C</h3>
<p class="report-text" style="left:110px">Lorem Ipsum is simply dummy text of the printing and typesetting industry. Lorem Ipsum has been the industry's standard dummy text ever</p>
<p class="report-text" style="left:446px">Lorem Ipsum is simply dummy text of the printing and typesetting industry. Lorem Ipsum has been the industry's standard dummy text ever</p>
<p class="report-text" style="left:780px">Lorem Ipsum is simply dummy text of the printing and typesetting industry. Lorem Ipsum has been the industry's standard dummy text ever</p>
<a class="btn report-btn" style="left:112px">Request Property Report A</a>
<a class="btn report-btn" style="left:446px">Request Property Report B</a>
<a class="btn report-btn" style="left:782px">Request Property Report C</a>

<section class="feature" role="img" aria-label="Smiling family sitting on a lawn in front of their home">
  <div class="feature-panel">
    <h2>Property<br>Development<br>Report</h2>
    <p>Lorem Ipsum is simply dummy text of the printing and typesetting industry. Lorem Ipsum has been the industry's standard dummy text ever since the 1500s, when an unknown printer took a galley of type and scrambled</p>
    <a class="btn">Read More</a>
  </div>
</section>

<h2 class="col-title" style="left:104px">PROPERTY REPORT PAGES</h2>
<h2 class="col-title" style="left:672px">OPPORTUNITIES WE PROVIDES</h2>

<div class="page-thumb" style="top:1986px;background:linear-gradient(135deg,#dfe6ec,#9fb0bf)" role="img" aria-label="Advisor meeting with a senior couple"></div>
<h3 class="page-title" style="top:1980px">Integer augue malesuada</h3>
<p class="page-text" style="top:2006px">iaculis ipsum dui aliquet felis at cursus magna nisl nec elit Praesent elementum elit at tellus nec ultricies sit amet porttitor mattis enim in massa libero interdum nec interdum vel blandit sed nulla in ullamcorper est eget tempor cursus</p>
<a class="link" style="left:272px;top:2092px">Read More</a>

<div class="page-thumb" style="top:2154px;background:linear-gradient(135deg,#3b3230,#c9bfb6)" role="img" aria-label="Two people in a consultation at a desk"></div>
<h3 class="page-title" style="top:2148px">Donec dictum lectus</h3>
<p class="page-text" style="top:2174px">iaculis ipsum dui aliquet felis at cursus magna nisl nec elit Praesent elementum elit at tellus nec ultricies sit amet porttitor mattis enim in massa libero interdum nec interdum vel blandit sed nulla in ullamcorper est eget tempor cursus</p>
<a class="link" style="left:272px;top:2260px">Read More</a>

<svg class="tick" style="top:1980px" viewBox="0 0 26 26"><circle cx="13" cy="13" r="13" fill="#1a9a72"/><path d="M7 13.5l4 4 8-8" fill="none" stroke="#fff" stroke-width="2.6"/></svg>
<h3 class="opp-title" style="top:1978px;font-weight:400">Altricies sit amet porttitor mattis</h3>
<p class="opp-text" style="top:2006px">enim in massa libero interdum nec interdum vel blandit sed</p>

<svg class="tick" style="top:2056px" viewBox="0 0 26 26"><circle cx="13" cy="13" r="13" fill="#1a9a72"/><path d="M7 13.5l4 4 8-8" fill="none" stroke="#fff" stroke-width="2.6"/></svg>
<h3 class="opp-title" style="top:2054px;font-weight:400">Cum sociis natoque penatibus et magnis</h3>
<p class="opp-text" style="top:2082px">Cras a ante vitae enim iaculis aliquam Mauris nunc quam ven enatis nec euismod sit amet egestas placerat</p>

<svg class="tick" style="top:2146px" viewBox="0 0 26 26"><circle cx="13" cy="13" r="13" fill="#1a9a72"/><path d="M7 13.5l4 4 8-8" fill="none" stroke="#fff" stroke-width="2.6"/></svg>
<h3 class="opp-title" style="top:2146px;font-weight:400">Lorem ipsum dolor sit amet</h3>
<p class="opp-text" style="top:2174px">enim in massa libero interdum nec interdum vel blandit sed</p>

<svg class="tick" style="top:2216px" viewBox="0 0 26 26"><circle cx="13" cy="13" r="13" fill="#1a9a72"/><path d="M7 13.5l4 4 8-8" fill="none" stroke="#fff" stroke-width="2.6"/></svg>
<h3 class="opp-title" style="top:2214px;font-weight:400">Mauris vel lacus vitae felis</h3>
<p class="opp-text" style="top:2242px">enim in massa libero interdum nec interdum vel blandit sed</p>

<section class="about">
  <h2 class="section-title" style="top:52px;color:#333">ABOUT US</h2>

  <svg class="about-icon" style="left:116px;top:130px" viewBox="0 0 56 56"><path d="M18 36h20M19 34V20M20 31l6-6 4 4 7-8" fill="none" stroke="#1a9a72" stroke-width="2"/></svg>
  <h3 class="about-head" style="left:190px;top:144px"><b>WHO</b> are we?</h3>
  <p class="about-text" style="left:112px;top:196px">Lorem Ipsum is simply dummy text of the printing and typesetting industry. Lorem Ipsum has been the industry's standard dummy text ever since the 1500s, when an unknown printer took a galley of type and scrambled it to make a type specimen book.</p>
  <a class="link" style="left:112px;top:326px">Read More</a>

  <svg class="about-icon" style="left:446px;top:130px" viewBox="0 0 56 56"><circle cx="28" cy="28" r="11" fill="none" stroke="#1a9a72" stroke-width="2"/><text x="28" y="33" text-anchor="middle" font-family="Open Sans, sans-serif" font-size="14" font-weight="700" fill="#1a9a72">$</text></svg>
  <h3 class="about-head" style="left:520px;top:144px"><b>WHAT</b> do we do?</h3>
  <p class="about-text" style="left:448px;top:196px">Lorem Ipsum is simply dummy text of the printing and typesetting industry. Lorem Ipsum has been the industry's standard dummy text ever since the 1500s, when an unknown printer took a galley of type and scrambled it to make a type specimen book.</p>
  <a class="link" style="left:448px;top:326px">Read More</a>

  <svg class="about-icon" style="left:780px;top:130px" viewBox="0 0 56 56"><path d="M18 28l10-9 10 9M21 26v10h5v-6h4v6h5V26" fill="#1a9a72"/></svg>
  <h3 class="about-head" style="left:854px;top:144px"><b>HOW</b> do we do it?</h3>
  <p class="about-text" style="left:782px;top:196px">Lorem Ipsum is simply dummy text of the printing and typesetting industry. Lorem Ipsum has been the industry's standard dummy text ever since the 1500s, when an unknown printer took a galley of type and scrambled it to make a type specimen book.</p>
  <a class="link" style="left:782px;top:326px">Read More</a>
</section>

<footer class="site-footer">
  <h4 class="foot-title" style="left:70px">About Us</h4>
  <ul class="foot-list chev" style="left:70px;top:70px">
    <li>WHO are we?</li><li>WHAT do we do?</li><li>HOW do we do it?</li>
  </ul>

  <h4 class="foot-title" style="left:302px">Social Media</h4>
  <ul class="foot-list social" style="left:304px;top:70px;line-height:25px">
    <li>Friendpage</li><li>Chirpline</li><li>Pinboard</li><li>Circles Plus</li>
  </ul>

  <h4 class="foot-title" style="left:476px">Contact Us</h4>
  <div class="abs" style="left:476px;top:80px;font-size:12px;line-height:20px">
    <svg width="12" height="9" viewBox="0 0 12 9" style="margin-right:6px"><rect width="12" height="9" fill="#ddd"/><path d="M0 0l6 5 6-5" fill="none" stroke="#1e1e1e" stroke-width="1.2"/></svg>Email<br>hello@qrbtappraisals.example
  </div>

  <div class="foot-brand">QRBT</div>
  <div class="search-label">Search</div>
  <div class="search-field"><div class="search-go">
    <svg width="38" height="34" viewBox="0 0 38 34"><circle cx="18" cy="16" r="5" fill="none" stroke="#fff" stroke-width="2"/><line x1="21.5" y1="19.5" x2="25" y2="23" stroke="#fff" stroke-width="2"/></svg>
  </div></div>
  <div class="foot-small">FAQ &nbsp;&nbsp;|&nbsp;&nbsp; Sitemap</div>
</footer>
<div class="footer-base">©2015 Northwind - Terms of Service - Privacy - Program Policies</div>

</body>
</html>
```